Australian Consulting Business Specialising in People and Process Consulting with Bluechip clients n

We are looking for designs using the logo as attached for letterhead and business cards that can be carried through to website in order to achieve consistency of style and hence recognition. It does not have to be overly suggestive but rather clean, crisp and professional.

The details are as follows:
Business Cards

Front Side
Brett Halloran
Director
M. 0427 305 612
E. brett@pinnockhallorran.com.au
W. www.pinnockhalloran.com.au

Warren pinnock
Director
M. 0433 571 920
E. warren@pinnockhallorran.com.au

Business Cards
Flip Side
Key Offerings

People Culture Process Growth
Development Analytics Improvement Strategies

Letter Head Details
Logo
Corporate Details
Pinnock Halloran Pty Ltd
PO Box 83
Kelvindale VIC 3287
Tel 61 3 9274 5808
info@pinnockhalloran.com.au
ACN 253917604
ABN 72016458391

```html
<!DOCTYPE html>
<html lang="en">
<head>
<meta charset="utf-8">
<title>Pinnock Halloran – Stationery</title>
<link rel="stylesheet" href="https://fonts.googleapis.com/css2?family=Montserrat:wght@700&family=Roboto:wght@400;500&display=swap">
<style>
  :root {
    --board: #dadada;
    --card: #f1f1f1;
    --paper: #ffffff;
    --orange: #f39200;
    --blue: #1b6fb8;
    --ink: #4a4a4a;
    --grey-mark: #707070;
  }
  * { box-sizing: border-box; margin: 0; padding: 0; }
  html, body { width: 911px; height: 1200px; overflow: hidden; }
  body {
    position: relative;
    background: var(--board);
    font-family: "Roboto", Arial, sans-serif;
    color: var(--ink);
  }
  .panel { position: absolute; overflow: hidden; }

  /* Business card front */
  .card-front { background: var(--card); width: 463px; height: 264px; }
  .card-front .block { position: absolute; left: 76px; width: 139px; }
  .card-front .block--orange { top: 0; height: 100px; background: var(--orange); }
  .card-front .block--blue { bottom: 0; height: 106px; background: var(--blue); }
  .card-front .contact-top {
    position: absolute; right: 12px; top: 22px;
    text-align: right; font-size: 13.5px; line-height: 18px; letter-spacing: .2px;
  }
  .card-front .contact-bottom {
    position: absolute; right: 8px; bottom: 14px;
    text-align: right; font-size: 13px; line-height: 18px; letter-spacing: .3px;
  }
  .card-front .wordmark { position: absolute; left: 12px; top: 113px; }

  /* Wordmark */
  .wordmark { display: flex; align-items: center; gap: 8px; }
  .wordmark .dot { width: 34px; height: 34px; border-radius: 50%; background: var(--orange); flex: none; }
  .wordmark .name {
    font-family: "Montserrat", Arial, sans-serif; font-weight: 700;
    color: var(--blue); font-size: 24px; letter-spacing: .3px; white-space: nowrap;
  }
  .wordmark--small .dot { width: 22px; height: 22px; }
  .wordmark--small .name { font-size: 15.5px; }
  .wordmark--tiny { gap: 5px; }
  .wordmark--tiny .dot { width: 16px; height: 16px; }
  .wordmark--tiny .name { font-size: 10.5px; }

  /* Card back */
  .card-back { background: var(--card); width: 453px; height: 264px; }
  .card-back .rule { position: absolute; top: 81px; height: 7px; }
  .card-back .rule--orange { left: 0; width: 167px; background: var(--orange); }
  .card-back .rule--blue { right: 0; width: 167px; background: var(--blue); }
  .card-back .heading { position: absolute; top: 76px; left: 0; right: 0; text-align: center; font-size: 13.5px; }
  .card-back .offerings {
    position: absolute; top: 118px; left: 0; right: 0; text-align: center;
    font-size: 13.5px; line-height: 16px; word-spacing: 2px;
  }
  .card-back .wordmark { position: absolute; top: 217px; left: 0; right: 0; justify-content: center; }

  /* Mockup photo areas */
  .photo { background: linear-gradient(150deg, #6d4a2c, #3a2414); }
  .photo--warm { background: linear-gradient(160deg, #c39a63, #5a3a1e 70%, #2e1c0e); }
  .photo--grey { background: linear-gradient(135deg, #9a9a9a, #d8d8d8 55%, #8a8a8a); }

  /* Letterhead */
  .letterhead { background: var(--paper); width: 402px; height: 568px; }
  .letterhead .wordmark { position: absolute; right: 14px; top: 18px; }
  .letterhead .footer-rule { position: absolute; top: 516px; height: 4px; }
  .letterhead .footer-rule--blue { left: 0; width: 182px; background: var(--blue); }
  .letterhead .footer-rule--orange { right: 0; width: 180px; background: var(--orange); }
  .letterhead .footer-dot {
    position: absolute; top: 508px; left: 190px; width: 20px; height: 20px;
    border-radius: 50%; background: var(--orange);
  }
  .letterhead .corporate {
    position: absolute; top: 530px; left: 0; right: 0; text-align: center;
    font-size: 7.6px; line-height: 10px; font-weight: 500; color: #555;
  }
</style>
</head>
<body>

  <section class="panel card-front" style="left:20px;top:22px;">
    <div class="block block--orange"></div>
    <div class="block block--blue"></div>
    <div class="contact-top">Warren Pinnock<br>Director<br>M. 0433 571 920</div>
    <div class="wordmark"><span class="dot"></span><span class="name">PINNOCK HALLORAN</span></div>
    <div class="contact-bottom">E. warren@pinnockhallorran.com.au<br>W. www.pinnockhalloran.com.au</div>
  </section>

  <div class="panel photo" role="img" aria-label="Photo of the business cards on a wooden desk beside a keyboard" style="left:493px;top:22px;width:397px;height:264px;"></div>

  <section class="panel card-front" style="left:20px;top:316px;height:273px;">
    <div class="block block--orange" style="height:108px"></div>
    <div class="block block--blue"></div>
    <div class="contact-top">Brett Halloran<br>Director<br>M. 0427 305 612</div>
    <div class="wordmark" style="top:118px"><span class="dot"></span><span class="name">PINNOCK HALLORAN</span></div>
    <div class="contact-bottom">E. brett@pinnockhallorran.com.au<br>W. www.pinnockhalloran.com.au</div>
  </section>

  <div class="panel photo photo--warm" role="img" aria-label="Photo of stacked business cards on a wooden table" style="left:493px;top:316px;width:397px;height:273px;"></div>

  <section class="panel card-back" style="left:20px;top:612px;">
    <div class="rule rule--orange"></div>
    <div class="rule rule--blue"></div>
    <div class="heading">Key Offerings</div>
    <div class="offerings">People Culture &nbsp;&nbsp;Process &nbsp;&nbsp;Growth<br>Development Analytics Improvement Strategies</div>
    <div class="wordmark wordmark--small"><span class="dot"></span><span class="name">PINNOCK HALLORAN</span></div>
  </section>

  <div class="panel photo photo--grey" role="img" aria-label="Photo of the letterhead stack seen at an angle" style="left:24px;top:889px;width:450px;height:289px;"></div>

  <section class="panel letterhead" style="left:493px;top:612px;">
    <div class="wordmark wordmark--tiny"><span class="dot"></span><span class="name">PINNOCK HALLORAN</span></div>
    <div class="footer-rule footer-rule--blue"></div>
    <div class="footer-dot"></div>
    <div class="footer-rule footer-rule--orange"></div>
    <div class="corporate">
      Pinnock Halloran Pty Ltd - PO Box 83 - Kelvindale VIC 3287<br>
      Tel 61 3 9274 5808 &nbsp;| &nbsp;info@pinnockhalloran.com.au<br>
      ACN 253917604 | &nbsp;ABN 72016458391
    </div>
  </section>

</body>
</html>
```